Business Card Design

Velora Pixel Outreach

An online marketing consulting & strategy business for the cosmetic niche

We specialise in Increasing Leads, Conversions & Content Marketing

I am looking for a very clean, BOLD business card that is simple & effective

Target Market(s)

cosmetic surgeons & cosmetic clinics

Industry/Entity Type

Marketing

Contact Information for Business Card

Brett Kaminski
Online Marketing Strategist

Brett@VeloraPixelOutreach.example
0491 268 530

LinkedIn: in/brettkaminski

```html
<!DOCTYPE html>
<html lang="en">
<head>
<meta charset="utf-8">
<title>Velora Pixel Outreach – Business Cards</title>
<link rel="stylesheet" href="https://fonts.googleapis.com/css2?family=Lato:wght@400;700;900&family=Saira+Semi+Expanded:wght@500&display=swap">
<style>
  :root {
    --bg: #e9e6df;
    --card: #ffffff;
    --teal: #1aa3c4;
    --green: #8cc63f;
    --grey: #6d6e71;
    --dark: #4d4e50;
    --faint: rgba(26, 163, 196, 0.10);
  }
  * { box-sizing: border-box; margin: 0; padding: 0; }
  html, body { width: 1200px; height: 1000px; overflow: hidden; }
  body { background: var(--bg); font-family: "Lato", sans-serif; position: relative; }

  .card {
    position: absolute;
    width: 620px; height: 354px;
    background: var(--card);
    box-shadow: 0 8px 24px rgba(0,0,0,0.18);
    overflow: hidden;
  }
  .card--front { left: 120px; top: 80px; }
  .card--back { left: 460px; top: 560px; }

  .edge-strip { position: absolute; width: 10px; }
  .card--front .edge-strip { right: 0; }
  .card--back .edge-strip { left: 0; }
  .edge-strip--blue { top: 0; height: 42%; background: var(--teal); }
  .edge-strip--green { bottom: 0; height: 42%; background: var(--green); }

  .brand { display: flex; align-items: center; gap: 18px; }
  .brand-dot { border-radius: 50%; background: var(--teal); flex: none; }
  .brand-name {
    font-family: "Saira Semi Expanded", sans-serif;
    font-weight: 500; color: var(--grey);
    text-transform: uppercase; line-height: 0.95;
  }

  .card--front .brand { position: absolute; left: 130px; top: 92px; }
  .card--front .brand-dot { width: 70px; height: 70px; }
  .card--front .brand-name { font-size: 38px; letter-spacing: 2px; }
  .front-tagline {
    position: absolute; left: 0; right: 0; bottom: 70px;
    text-align: center; font-weight: 900; font-size: 14.5px; color: var(--teal);
  }
  .front-tagline .amp { color: var(--green); }

  .deco-circle {
    position: absolute; right: -60px; top: -40px;
    width: 230px; height: 230px; border-radius: 50%;
    border: 26px solid var(--faint);
  }

  .card--back .brand { position: absolute; left: 48px; top: 52px; }
  .card--back .brand-dot { width: 44px; height: 44px; }
  .card--back .brand-name { font-size: 23px; letter-spacing: 1.5px; }
  .divider { position: absolute; width: 1.5px; background: var(--green); }
  .divider--top { left: 305px; top: 40px; height: 90px; }
  .divider--bottom { left: 290px; top: 240px; height: 80px; }
  .specialty {
    position: absolute; left: 325px; top: 50px; width: 270px;
    font-weight: 900; font-size: 15px; line-height: 1.25; color: var(--teal);
  }
  .person { position: absolute; left: 50px; top: 262px; }
  .person-name { font-weight: 700; font-size: 27px; color: var(--teal); }
  .person-title { font-weight: 700; font-size: 17px; color: var(--grey); }
  .contact {
    position: absolute; left: 305px; top: 255px;
    font-weight: 700; font-size: 14.5px; color: var(--dark); line-height: 1.45;
  }
  .contact .sep { color: var(--grey); margin: 0 6px; }
  .contact .label { color: var(--green); }
</style>
</head>
<body>

  <section class="card card--front" aria-label="Business card front">
    <span class="edge-strip edge-strip--blue"></span>
    <span class="edge-strip edge-strip--green"></span>
    <div class="brand">
      <span class="brand-dot"></span>
      <p class="brand-name">Velora<br>Pixel<br>Outreach</p>
    </div>
    <p class="front-tagline">Online Marketing Consulting <span class="amp">&amp;</span> Strategy Business For The Cosmetic Niche</p>
  </section>

  <section class="card card--back" aria-label="Business card back">
    <span class="edge-strip edge-strip--blue"></span>
    <span class="edge-strip edge-strip--green"></span>
    <span class="deco-circle"></span>
    <div class="brand">
      <span class="brand-dot"></span>
      <p class="brand-name">Velora<br>Pixel<br>Outreach</p>
    </div>
    <span class="divider divider--top"></span>
    <p class="specialty">Specialized in Increasing Leads,<br>Conversions &amp; Content Marketing</p>
    <div class="person">
      <p class="person-name">Brett Kaminski</p>
      <p class="person-title">Online Marketing Strategist</p>
    </div>
    <span class="divider divider--bottom"></span>
    <div class="contact">
      <p>0491 268 530<span class="sep">|</span><span class="label">linkedIn:</span> in/brettkaminski</p>
      <p>Brett@VeloraPixelOutreach.example</p>
    </div>
  </section>

</body>
</html>
```